We have a new logo so we need to change our business card

We're super Happy with our current cards but I think with a new logo should come a new design. I wouldn't mind seeing the icons that we used on the back last time reused on this card. Please feel free to visit our website to get a sense for our brand www.brindlewick.ca

I need the final final to have contact info for:

Gordon Hasley
Co-Owner
info@brindlewick.ca
778-315-6207

and

Marjorie Hasley
Co-Owner
info@brindlewick.ca
778-342-5810

Target Market(s)

Female dog owners, 21 to 70

Industry/Entity Type

pet industry

Contact Information for Business Card

included in brief

Requirements
Should not have
• We do not want it to look cartonish

```html
<!DOCTYPE html>
<html lang="en">
<head>
<meta charset="utf-8">
<title>Brindlewick Business Card</title>
<link href="https://fonts.googleapis.com/css2?family=Open+Sans:wght@400;700;800&family=Arimo:wght@400&display=swap" rel="stylesheet">
<style>
  :root {
    --page-bg: #d6d6d6;
    --card-white: #ffffff;
    --brand-green: #96cc5e;
    --deep-green: #3b5a22;
    --ink: #1b1b1b;
    --rule: #b9b9b9;
  }
  * { margin: 0; padding: 0; box-sizing: border-box; }
  html, body { width: 1200px; height: 800px; overflow: hidden; }
  body {
    background: var(--page-bg);
    position: relative;
    font-family: "Open Sans", sans-serif;
  }
  .card {
    position: absolute;
    top: 245px;
    width: 540px;
    height: 309px;
    box-shadow: 0 10px 30px rgba(0,0,0,0.18);
  }
  .card-front { left: 40px; background: var(--card-white); }
  .card-back { left: 620px; background: var(--brand-green); }

  .brand {
    position: absolute;
    display: flex;
    align-items: center;
    gap: 12px;
    white-space: nowrap;
  }
  .brand-dot {
    border-radius: 50%;
    flex: none;
  }
  .brand-name {
    font-family: "Open Sans", sans-serif;
    font-weight: 800;
    letter-spacing: -0.5px;
  }
  .card-front .brand { left: 36px; top: 128px; }
  .card-front .brand-dot { width: 54px; height: 54px; background: var(--brand-green); }
  .card-front .brand-name { color: var(--ink); font-size: 29px; }

  .divider {
    position: absolute;
    left: 318px; top: 88px;
    width: 1px; height: 132px;
    background: var(--rule);
  }

  .contact { position: absolute; left: 338px; top: 92px; }
  .contact-name {
    color: var(--brand-green);
    font-weight: 700;
    font-size: 21px;
    line-height: 1.1;
    white-space: nowrap;
  }
  .contact-role {
    font-family: "Arimo", sans-serif;
    color: var(--ink);
    font-size: 14px;
    margin: 2px 0 12px;
  }
  .contact-list { list-style: none; }
  .contact-list li {
    font-family: "Arimo", sans-serif;
    color: var(--ink);
    font-size: 13px;
    display: flex;
    align-items: center;
    gap: 7px;
    margin-bottom: 5px;
    white-space: nowrap;
  }
  .contact-list svg { width: 13px; height: 13px; flex: none; }

  .card-back .brand {
    left: 50%; top: 50%;
    transform: translate(-50%, -50%);
    gap: 16px;
  }
  .card-back .brand-dot { width: 80px; height: 80px; background: var(--deep-green); }
  .card-back .brand-name { color: var(--deep-green); font-size: 46px; }
</style>
</head>
<body>
  <section class="card card-front">
    <div class="brand">
      <span class="brand-dot"></span>
      <span class="brand-name">Brindlewick</span>
    </div>
    <div class="divider"></div>
    <div class="contact">
      <p class="contact-name">Gordon Hasley</p>
      <p class="contact-role">Co-Owner</p>
      <ul class="contact-list">
        <li>
          <svg viewBox="0 0 16 16" aria-hidden="true"><path fill="#96cc5e" d="M3.5 1.5l2.5 0 1 3.5-1.6 1.2a8 8 0 0 0 4.4 4.4L11 9l3.5 1v2.5c0 .8-.7 1.5-1.5 1.5C7 14 2 9 2 3c0-.8.7-1.5 1.5-1.5z"/></svg>
          778-315-6207
        </li>
        <li>
          <svg viewBox="0 0 16 16" aria-hidden="true"><rect x="1" y="3.5" width="14" height="9" fill="#96cc5e"/><path d="M1.5 4l6.5 5 6.5-5" fill="none" stroke="#fff" stroke-width="1.2"/></svg>
          info@brindlewick.ca
        </li>
        <li>
          <svg viewBox="0 0 16 16" aria-hidden="true"><circle cx="8" cy="8" r="7" fill="#96cc5e"/><g fill="none" stroke="#fff" stroke-width="0.9"><ellipse cx="8" cy="8" rx="3" ry="7"/><path d="M1 8h14M2.5 4.5h11M2.5 11.5h11"/></g></svg>
          www.brindlewick.ca
        </li>
      </ul>
    </div>
  </section>

  <section class="card card-back">
    <div class="brand">
      <span class="brand-dot"></span>
      <span class="brand-name">Brindlewick</span>
    </div>
  </section>
</body>
</html>
```